Presentation & Communication (Guide, Ebook, carroussel lumivo, tralvex et plazmora)

Suite à la conception du logo, je souhaite désormais développer une identité visuelle complète ainsi que des supports marketing pour ma page Plazmora, ma communication client interne notamment :
- Couverture Plazmora + Photo de profil Plazmora
- Guides
- E-books
- Et enfin, une charte graphique destinée aux formulaires sous format Microsoft Forms (pour la collecte de sondages et la prospection).
Vous trouverez ci-joint le logo que vous avez créé, ainsi qu’une couverture que j’ai réalisée via Canva. Cependant, lors de l’importation sur Plazmora, le logo et les illustrations apparaissent flous.
Rappel important :
La direction artistique et l’identité visuelle doivent être en parfaite cohérence avec le logo et l’activité, à savoir :
un cabinet d’expertise comptable spécialisé pour les chirurgiens-dentistes et les centres dentaires. Je souhaite quelque chose de minimaliste, haut de gamme et moderne (je veux pas des logos de dents et d'instrument grossier et dans tous les sens).
Les couleurs qui ont été utilisées pour le site sont principalement : #0F1121 ; #FFFFFF ; #4A90A4 ; #5FAFB3.
Les supports doivent être téléchargeable sous format pack office de façon à pouvoir les utiliser et rédiger dessus du texte (guides, e-books, image pour post réseaux sociaux). Il faut donc déterminer une police efficace qui correspond à l'image de mon cabinet comptable (Poppins peut être ?)
Ce que j'aimerais :
1) Une visuel de page de couverture Plaz mora
2) Un visuel d'image de profil (Icône) de page Plazmora / Lumivo de mon logo
3) Un visuel moderne, haut de gamme et élégant au bon format en utilsant en partie les couleurs évoqué dans le brief. Ce visuel doit être adaptée au format Post publication Lumivo et Plazmora avec un visuel autour mais avec la possibilité d'écrire du texte sur le support que vous créér (exemple pièce jointe d'un confrère à moi)
4) Un support Guide de façon également à rédiger dessus simplement avec une bonne typographie moderne et professionnelle, sur plusieurs pages à minima sur 10 pages. Je demande un peu la création d'un thème sous format pack office pour simplifier l'utilisation du fichier et le process pour uniquement éditer et importer sur Tralvex, Plazmora et Lumivo sans transformer ou redymensionner ou rogner la qualité du support. (Deux Exemples ci-joint).
5) Créer un Ebook de la même manière avec un fond (un thème) qui représente bien mon cabinet haut de gamme, classe et moderne. (Exemple Ebook ci-joint)
English :
Following the logo design, I now wish to develop a complete visual identity and marketing materials for my Plazmora page and internal client communications, including:
- Plazmora cover photo + Plazmora profile picture
- Guides
- E-books
- And finally, a style guide for Microsoft Forms forms (for survey collection and lead generation).
Attached you will find the logo you created, as well as a cover photo I designed using Canva. However, when uploaded to Plazmora, the logo and illustrations appear blurry.
Important reminder:
The art direction and visual identity must be perfectly consistent with the logo and the business activity, namely:
an accounting firm specializing in services for dentists and dental clinics. I want something minimalist, high-end, and modern (I don't want logos of teeth and crude instruments in all directions).
The colors used for the website are primarily: #0F1121; #FFFFFF; #4A90A4; #5FAFB3.
The materials must be downloadable in Microsoft Office format so they can be used and text added to (guides, e-books, images for social media posts). Therefore, an effective font that matches my accounting firm's image needs to be chosen (Poppins, perhaps?).
What I would like:
1) A Plazmora cover image
2) A Plazmora/Lumivo profile picture (icon) of my logo
3) A modern, high-end, and elegant image in the correct format, partially using the colors mentioned in the brief. This image must be suitable for Lumivo and Plazmora posts, with a surrounding image, but with the option to write text on the document you create (example attached from a colleague).
4) A guide template, also easy to write on, with good, modern, and professional typography, spanning at least 10 pages. I would like a template created in Microsoft Office format to simplify file use and the process of simply editing and importing it to Tralvex, Plazmora, and Lumivo without transforming, resizing, or cropping the document. (Two examples attached).
5) Create an ebook in the same style with a background (theme) that accurately represents my high-end, classy, and modern firm. (Example ebook attached)
Target Market(s)
Chirurgiens dentistes, orthodontistes
Industry/Entity Type
Expertise comptable et conseil fiscal

```html
<!DOCTYPE html>
<html lang="en">
<head>
<meta charset="utf-8">
<title>Nerovia Identity Design</title>
<link href="https://fonts.googleapis.com/css2?family=Montserrat:wght@300;400;500;600;700;800&display=swap" rel="stylesheet">
<style>
  :root{
    --header:#2c2a68;
    --ink:#14132b;
    --ink-deep:#101024;
    --violet:#2e2b6a;
    --violet-soft:#403a86;
    --lilac:#6a63bf;
    --cream:#e6e0cf;
    --cream-line:#d8d0b8;
    --label:#2a2a2a;
    --page-bg-top:#eeeeee;
    --page-bg-bottom:#ffffff;
  }
  *{margin:0;padding:0;box-sizing:border-box;}
  html,body{width:1200px;height:4000px;overflow:hidden;}
  body{
    font-family:"Montserrat",sans-serif;
    background:linear-gradient(160deg,var(--page-bg-top) 0%,#e9e9e9 45%,var(--page-bg-bottom) 100%);
    position:relative;
    color:var(--label);
  }
  .header{
    position:absolute;left:0;top:0;width:1200px;height:204px;
    background:var(--header);
    display:flex;align-items:center;justify-content:center;
    box-shadow:0 14px 30px rgba(0,0,0,.18);
  }
  .header h1{font-weight:300;font-size:68px;letter-spacing:3px;color:var(--cream);}
  .section-label{position:absolute;font-weight:300;font-size:40px;color:var(--label);letter-spacing:.5px;}

  /* cover */
  .cover{position:absolute;left:126px;top:354px;width:949px;height:360px;background:var(--ink);overflow:hidden;}
  .cover-pattern{position:absolute;right:0;top:0;width:484px;height:360px;
    background:linear-gradient(100deg,var(--ink) 0%,#1e1c3c 45%,#24224a 100%);}
  .cover-mark{position:absolute;left:278px;top:101px;width:124px;height:124px;border:9px solid var(--cream);border-radius:50%;}
  .cover-name{position:absolute;left:422px;top:150px;font-size:62px;font-weight:400;color:var(--cream);letter-spacing:2px;line-height:1;}
  .cover-sub{position:absolute;left:400px;top:211px;font-size:13px;font-weight:400;color:var(--cream);letter-spacing:.5px;}
  .cover-bar{position:absolute;left:0;top:292px;width:282px;height:25px;background:var(--violet);}
  .cover-tagline{position:absolute;left:298px;top:291px;width:349px;height:27px;background:var(--cream);
    border-radius:0 14px 14px 0;font-size:11px;color:var(--ink);display:flex;align-items:center;justify-content:center;letter-spacing:.1px;white-space:nowrap;}

  /* profile */
  .profile{position:absolute;border-radius:50%;display:flex;align-items:center;justify-content:center;
    font-weight:600;font-size:30px;letter-spacing:1.5px;}
  .profile--dark{left:121px;top:895px;width:214px;height:214px;background:var(--ink);color:var(--cream);}
  .profile--light{left:366px;top:893px;width:218px;height:218px;background:var(--cream);color:var(--ink);
    border:6px solid #ffffff;box-shadow:0 0 0 1px #e0e0e0;}

  /* social posts */
  .post{position:absolute;top:1295px;width:439px;height:550px;overflow:hidden;background:var(--ink);}
  .post--one{left:134px;}
  .post--two{left:634px;}
  .post svg{position:absolute;left:0;top:0;}
  .post-brand{position:absolute;left:22px;top:24px;display:flex;align-items:center;gap:6px;
    font-size:11px;font-weight:600;color:var(--cream);letter-spacing:1px;}
  .post-brand .dot{width:26px;height:26px;border:3px solid var(--cream);border-radius:50%;}
  .post-title{position:absolute;left:0;width:100%;top:425px;text-align:center;font-size:40px;font-weight:800;color:var(--ink);line-height:1;}
  .post-sub{position:absolute;left:0;width:100%;top:470px;text-align:center;font-size:29px;font-weight:300;color:var(--ink);}
  .post-web{position:absolute;right:0;top:524px;height:16px;padding:0 10px 0 4px;background:#ffffff;border-radius:8px 0 0 8px;
    display:flex;align-items:center;gap:5px;font-size:9px;color:var(--ink);}
  .post-web .dot{width:11px;height:11px;border-radius:50%;background:var(--violet);}

  /* guide pages */
  .guide{position:absolute;left:134px;width:613px;height:867px;overflow:hidden;background:var(--ink);}
  .guide--one{top:2045px;}
  .guide--two{top:2954px;}
  .guide svg{position:absolute;left:0;top:0;}
  .guide-brand{position:absolute;left:0;width:100%;top:28px;display:flex;flex-direction:column;align-items:center;gap:4px;
    font-size:10px;font-weight:600;letter-spacing:1px;color:var(--ink);}
  .guide-brand .dot{width:30px;height:30px;border:3px solid var(--ink);border-radius:50%;}
  .guide-title{position:absolute;left:0;width:100%;top:108px;text-align:center;font-size:46px;font-weight:700;color:var(--ink);}
  .guide-kicker{position:absolute;left:0;width:100%;top:167px;display:flex;justify-content:center;align-items:center;gap:22px;
    font-size:22px;font-weight:300;color:var(--ink);}
  .guide-kicker::before,.guide-kicker::after{content:"";width:50px;height:2px;background:var(--ink);}
  .guide-frame{position:absolute;left:105px;top:228px;width:404px;height:295px;background:var(--violet);
    display:flex;align-items:center;justify-content:center;text-align:center;font-size:28px;font-weight:300;line-height:1.25;color:var(--lilac);}
  .guide-marker{position:absolute;left:100px;top:519px;width:10px;height:10px;background:var(--cream);}
  .guide-block{position:absolute;left:105px;width:404px;font-size:11.6px;line-height:14.8px;font-weight:400;}
  .guide-block h2{font-size:15.5px;font-weight:600;margin-bottom:3px;display:flex;align-items:center;gap:6px;}
  .guide-block h2::before{content:"";width:11px;height:11px;background:currentColor;}
  .guide-block--light{color:var(--cream);}
  .guide-block--light h2::before{background:var(--cream);}
  .guide-block--dark{color:var(--ink);}
  .guide-block--dark h2::before{background:var(--violet);}
  .guide-note{position:absolute;left:105px;width:404px;top:686px;text-align:center;font-size:11.6px;line-height:14.8px;font-weight:600;color:#ffffff;}
  .guide-footer{position:absolute;left:0;top:827px;display:flex;align-items:center;gap:7px;}
  .guide-footer .num{width:50px;height:24px;background:var(--cream);color:var(--ink);font-weight:700;font-size:16px;
    display:flex;align-items:center;justify-content:flex-end;padding-right:8px;}
  .guide-footer .sub{height:22px;padding:0 10px;background:var(--violet);border-radius:0 11px 11px 0;color:#b6b1e6;font-size:10.5px;
    display:flex;align-items:center;}
  .guide-corner{position:absolute;left:563px;top:822px;width:32px;height:32px;border:3px solid var(--cream);border-radius:50%;}
</style>
</head>
<body>

<header class="header"><h1>NEROVIA IDENTITY DESIGN</h1></header>

<!-- Cover -->
<p class="section-label" style="left:121px;top:285px;">Plazmora cover:</p>
<section class="cover">
  <div class="cover-pattern" role="img" aria-label="Subtle geometric arch pattern in deep navy"></div>
  <div class="cover-mark"></div>
  <div class="cover-name">NEROVIA</div>
  <div class="cover-sub">EXPERTISE COMPTABLE ET CONSEIL</div>
  <div class="cover-bar"></div>
  <div class="cover-tagline">VOS PROJETS, NOTRE RIGUEUR POUR LES ACCOMPAGNER</div>
</section>

<!-- Profile -->
<p class="section-label" style="left:126px;top:816px;">Profile:</p>
<div class="profile profile--dark">NEROVIA</div>
<div class="profile profile--light">NEROVIA</div>

<!-- Social posts -->
<p class="section-label" style="left:131px;top:1220px;">Social Media Cover:</p>

<section class="post post--one">
  <svg width="439" height="550" viewBox="0 0 439 550">
    <defs>
      <linearGradient id="patternFade1" x1="0" y1="0" x2="1" y2="1">
        <stop offset="0" stop-color="#14132b"/><stop offset="1" stop-color="#22204a"/>
      </linearGradient>
      <linearGradient id="photoHands" x1="0" y1="0" x2="0" y2="1">
        <stop offset="0" stop-color="#4a4390"/><stop offset=".55" stop-color="#5a4f8a"/><stop offset="1" stop-color="#2e2b5a"/>
      </linearGradient>
    </defs>
    <rect x="260" y="0" width="179" height="230" fill="url(#patternFade1)" role="img" aria-label="Subtle geometric pattern"/>
    <path d="M88,550 L88,170 A135.5,135.5 0 0 1 359,170 L359,550 Z" fill="url(#photoHands)" role="img" aria-label="Photo of a business handshake"/>
    <path d="M0,290 C50,400 140,420 230,398 C310,380 380,368 439,380 L439,550 L0,550 Z" fill="var(--cream)"/>
  </svg>
  <div class="post-brand"><span class="dot"></span>NEROVIA</div>
  <div class="post-title">Your text</div>
  <div class="post-sub">will be placed here.</div>
  <div class="post-web"><span class="dot"></span>www.nerovia-expertise.fr</div>
</section>

<section class="post post--two">
  <svg width="439" height="550" viewBox="0 0 439 550">
    <defs>
      <linearGradient id="patternFade2" x1="0" y1="0" x2="1" y2="1">
        <stop offset="0" stop-color="#14132b"/><stop offset="1" stop-color="#22204a"/>
      </linearGradient>
      <linearGradient id="photoAdvisor" x1="0" y1="0" x2="0" y2="1">
        <stop offset="0" stop-color="#4a4390"/><stop offset=".5" stop-color="#2a2838"/><stop offset="1" stop-color="#1b1a26"/>
      </linearGradient>
    </defs>
    <rect x="260" y="0" width="179" height="230" fill="url(#patternFade2)" role="img" aria-label="Subtle geometric pattern"/>
    <path d="M88,550 L88,170 A135.5,135.5 0 0 1 359,170 L359,550 Z" fill="url(#photoAdvisor)" role="img" aria-label="Photo of an advisor in a dark coat writing in a notebook"/>
    <path d="M0,290 C50,400 140,420 230,398 C310,380 380,368 439,380 L439,550 L0,550 Z" fill="var(--cream)"/>
  </svg>
  <div class="post-brand"><span class="dot"></span>NEROVIA</div>
  <div class="post-title">Your text</div>
  <div class="post-sub">will be placed here.</div>
  <div class="post-web"><span class="dot"></span>www.nerovia-expertise.fr</div>
</section>

<!-- Guide template -->
<p class="section-label" style="left:131px;top:1964px;">Guid Template:</p>

<section class="guide guide--one">
  <svg width="613" height="867" viewBox="0 0 613 867">
    <defs>
      <linearGradient id="guideDark" x1="0" y1="0" x2="1" y2="1">
        <stop offset="0" stop-color="#101024"/><stop offset=".6" stop-color="#191838"/><stop offset="1" stop-color="#13122b"/>
      </linearGradient>
    </defs>
    <rect width="613" height="867" fill="url(#guideDark)"/>
    <path d="M0,0 H613 V285 C520,270 420,300 300,330 C180,360 60,330 0,290 Z" fill="var(--cream)"/>
  </svg>
  <div class="guide-brand"><span class="dot"></span>NEROVIA</div>
  <h1 class="guide-title">Guide template</h1>
  <div class="guide-kicker">this is sample Text</div>
  <div class="guide-frame">Text Or Image<br>in this frame</div>
  <div class="guide-marker"></div>
  <div class="guide-block guide-block--light" style="top:572px;">
    <h2>What is Lorem Ipsum?</h2>
    <p>Lorem Ipsum is simply dummy text of the printing and typesetting industry. Lorem Ipsum has been the industry's standard dummy text for a very long time, when an unnamed printer took a galley of type and scrambled it to make a type specimen book. It has survived not only many decades, but also the leap into electronic typesetting, remaining essentially unchanged. It became popular with the release of transfer sheets containing Lorem Ipsum passages, and more recently with desktop publishing software including versions of Lorem Ipsum.</p>
  </div>
  <div class="guide-footer"><span class="num">01</span><span class="sub">Sub Title of This page</span></div>
</section>

<section class="guide guide--two">
  <svg width="613" height="867" viewBox="0 0 613 867">
    <rect width="613" height="867" fill="var(--ink-deep)"/>
    <rect width="613" height="307" fill="var(--violet)"/>
    <path d="M53,307 H561 V560 A80,80 0 0 1 481,640 H133 A80,80 0 0 1 53,560 Z" fill="var(--cream)"/>
  </svg>
  <div class="guide-block guide-block--light" style="top:58px;">
    <h2>Why do we use it?</h2>
    <p>It is a long established fact that a reader will be distracted by the readable content of a page when looking at its layout. The point of using Lorem Ipsum is that it has a more-or-less normal distribution of letters, as opposed to using 'Content here, content here', making it look like readable English. Many desktop publishing packages and web page editors now use Lorem Ipsum as their default model text, and a search for 'lorem ipsum' will uncover many web sites still in their infancy. Various versions have evolved over the years, sometimes by accident, sometimes on purpose (injected humour and the like).</p>
  </div>
  <div class="guide-block guide-block--dark" style="top:358px;">
    <h2>Where does it come from?</h2>
    <p>Contrary to popular belief, Lorem Ipsum is not simply random text. It has roots in a piece of classical Latin literature, making it many centuries old. A Latin scholar looked up one of the more obscure Latin words, consectetur, from a Lorem Ipsum passage, and going through the cites of the word in classical literature, discovered the undoubtable source. Lorem Ipsum comes from two short sections of an ancient treatise on the extremes of good and evil, written long ago. This book is a treatise on the theory of ethics, very popular during the Renaissance. The first line of Lorem Ipsum, "Lorem ipsum dolor sit amet..", comes from a line in the first of these sections.</p>
  </div>
  <p class="guide-note">The standard chunk of Lorem Ipsum used for centuries is reproduced below for those interested. Both sections from the ancient treatise are also reproduced in their exact original form, accompanied by English versions from a translation made in the early twentieth century.</p>
  <div class="guide-footer"><span class="num">02</span><span class="sub">Sub Title of This page</span></div>
  <div class="guide-corner"></div>
</section>

</body>
</html>
```